Birchwood Forage Business Cards

I need a business card with my logo, number, Facebook account, and some information about what I am selling. Green card with logo on the front. 847-302-1596 phone number, @birchwoodforage Facebook, •Orchardgrass Hay •Alfalfa Hay •Mixed Grass Hay , and “Premium Quality Hay” all written on the back.

Target Market(s)

Hay

Contact Information for Business Card

Phone number, Facebook, different types of hay.

Colors
00AB8E
00BBA5
67D7C9
C6EFE9
E9F9F6

```html
<!DOCTYPE html>
<html lang="en">
<head>
<meta charset="utf-8">
<title>Birchwood Forage Business Cards</title>
<link href="https://fonts.googleapis.com/css2?family=Arimo:wght@400;700&family=Roboto:wght@400&display=swap" rel="stylesheet">
<style>
  :root {
    --stage: #2b2c2f;
    --card-white: #f7f7f7;
    --card-black: #0e0e0f;
    --brand-green: #16a84c;
    --ink: #111111;
    --paper-text: #ffffff;
    --rule: #d8d8d8;
    --icon-blue: #3b5cb8;
  }
  * { box-sizing: border-box; margin: 0; padding: 0; }
  html, body {
    width: 1200px; height: 781px; overflow: hidden;
    background: var(--stage);
  }
  .sheet {
    position: relative; width: 1200px; height: 781px;
    display: flex; align-items: center; justify-content: center; gap: 60px;
  }
  .card {
    position: relative; width: 500px; height: 286px;
    border-radius: 18px; overflow: hidden;
    box-shadow: 0 14px 30px rgba(0,0,0,.45);
  }
  .card svg.card-art { position: absolute; inset: 0; }

  /* front */
  .card--front { background: var(--card-white); }
  .brand {
    position: absolute; left: 46px; top: 46px;
    display: flex; align-items: center; gap: 14px;
  }
  .brand__dot {
    width: 50px; height: 50px; border-radius: 50%;
    background: var(--brand-green);
  }
  .brand__name {
    font-family: "Arimo", Arial, sans-serif; font-weight: 700;
    font-size: 34px; color: var(--ink);
  }
  .front-phone {
    position: absolute; left: 110px; top: 112px;
    font-family: "Arimo", Arial, sans-serif; font-weight: 700;
    font-size: 46px; letter-spacing: 1px; color: var(--ink);
  }
  .tagline {
    position: absolute; left: 64px; top: 236px;
    font-family: "Arimo", Arial, sans-serif; font-size: 18px;
    color: var(--paper-text);
  }

  /* back */
  .card--back {
    background: var(--card-black);
    font-family: "Roboto", Arial, sans-serif; color: var(--paper-text);
  }
  .contact-row {
    position: absolute; display: flex; align-items: center; gap: 10px;
  }
  .contact-row--phone { left: 30px; top: 26px; font-size: 14px; }
  .contact-row--social { left: 180px; top: 228px; font-size: 19px; }
  .icon-badge {
    width: 20px; height: 20px; border-radius: 50%;
    background: var(--icon-blue);
    display: flex; align-items: center; justify-content: center;
  }
  .contact-row--social .icon-badge { width: 26px; height: 26px; }
  .rule {
    position: absolute; height: 1px; background: var(--rule);
  }
  .rule--top { left: 168px; right: 26px; top: 44px; }
  .rule--bottom { left: 26px; width: 144px; top: 241px; }
  .rule--mid-top { left: 26px; right: 26px; top: 104px; opacity: 0; }
  .products {
    position: absolute; left: 0; right: 0; top: 128px;
    display: flex; justify-content: center; gap: 16px;
    font-size: 17px; white-space: nowrap;
  }
  .products .sep { opacity: .9; }
</style>
</head>
<body>
<main class="sheet">
  <section class="card card--front" aria-label="Card front">
    <svg class="card-art" width="500" height="286" viewBox="0 0 500 286" aria-hidden="true">
      <path d="M0,168 C150,215 320,232 500,206 L500,222 C320,246 150,232 0,186 Z" fill="#111"/>
      <path d="M0,184 C150,230 320,244 500,220 L500,286 L0,286 Z" fill="var(--brand-green)"/>
    </svg>
    <div class="brand">
      <span class="brand__dot"></span>
      <span class="brand__name">Birchwood Forage</span>
    </div>
    <div class="front-phone">847-302-1596</div>
    <div class="tagline">Premium Quality Hay</div>
  </section>

  <section class="card card--back" aria-label="Card back">
    <div class="contact-row contact-row--phone">
      <span class="icon-badge">
        <svg width="12" height="12" viewBox="0 0 24 24" aria-hidden="true">
          <path d="M6.6 10.8a15 15 0 0 0 6.6 6.6l2.2-2.2c.3-.3.7-.4 1-.2 1.1.4 2.3.6 3.6.6.6 0 1 .4 1 1V20c0 .6-.4 1-1 1C10.6 21 3 13.4 3 4c0-.6.4-1 1-1h3.5c.6 0 1 .4 1 1 0 1.3.2 2.5.6 3.6.1.3 0 .7-.2 1z" fill="#fff"/>
        </svg>
      </span>
      <span>847-302-1596</span>
    </div>
    <div class="rule rule--top"></div>

    <div class="products">
      <span>Orchardgrass Hay</span><span class="sep">|</span>
      <span>Alfalfa Hay</span><span class="sep">|</span>
      <span>Mixed Grass Hay</span>
    </div>

    <div class="rule rule--bottom"></div>
    <div class="contact-row contact-row--social">
      <span class="icon-badge"></span>
      <span>@birchwoodforage</span>
    </div>
  </section>
</main>
</body>
</html>
```